A Training Firm needs a Brochure - Steady Course Onboarding Learning Brochure

Tevaluma, a HR Consulting Firm focused on Training & Development is seeking a Brochure Design for one of its training programs - Steady Course Onboarding Learning Program.

The designs should be innovative,image led and interesting to read. We would like to see designs that incorporate the colours Blue and Green. Because this company is based in Africa, we would like the designers to use image of Black people instead of Caucasians.

Tevaluma is a member of Brightmere Group, a HR Consulting firm that offers services in the area of Learning, Talent Solutions, Outsourcing and Strategy Consulting

Target Market(s)

CEOs, HR Directors, Heads of Learning and Learning Managers of Large, Medium and Small Scale Organisations in Nigeria

Industry/Entity Type

Training

Other font styles liked:
• Corbel

Colors
3176b5
abd036

Requirements
Must have
• Tevaluma Logo, A link with the Parent Company Brightmere Group (We usually add that Tevaluma is a member of the Brightmere Group) The Group Logo and the Pantone Colours have been attached
Nice to have
• The entire Brochure should be graphically led. That is, lots of graphics - Infographics/Images/colours etc
Should not have
• No Caucasian images. We are an African based Firm and would like to have African images

```html
<!DOCTYPE html>
<html lang="en">
<head>
<meta charset="utf-8">
<title>Tevaluma – Steady Course Onboarding Learning Brochure</title>
<link rel="stylesheet" href="https://fonts.googleapis.com/css2?family=Open+Sans:wght@400;600;700&display=swap">
<style>
  :root {
    --backdrop: #e6e7e8;
    --teal-deep: #0d5468;
    --teal: #17707f;
    --teal-light: #2a8a98;
    --band: #ececec;
    --lime: #c9d98a;
    --graphite: #555859;
    --ink-teal: #136e82;
    --ink-grey: #5b5e60;
    --photo-warm: #b39a7a;
    --photo-cool: #8da2b5;
  }
  * { margin: 0; padding: 0; box-sizing: border-box; }
  html, body {
    width: 1200px; height: 873px; overflow: hidden;
    background: var(--backdrop);
    font-family: "Open Sans", Verdana, sans-serif;
  }
  .spread {
    position: absolute; left: 50px; top: 62px;
    width: 1100px; height: 750px;
    box-shadow: 0 8px 24px rgba(0,0,0,0.18);
    overflow: hidden;
  }
  .page {
    position: absolute; top: 0; width: 550px; height: 750px;
    background: linear-gradient(160deg, var(--teal-light) 0%, var(--teal) 35%, var(--teal-deep) 100%);
  }
  .page--back { left: 0; }
  .page--front { left: 550px; }
  .band { position: absolute; background: var(--band); }
  .band--contact { left: 0; top: 430px; width: 550px; height: 180px; }
  .band--title { left: 760px; top: 410px; width: 340px; height: 140px; }

  .tile { position: absolute; }
  .tile--lime { background: var(--lime); }
  .tile--graphite { background: var(--graphite); }
  .photo { position: absolute; outline: 2px solid var(--teal-deep); }
  .photo--warm { background: linear-gradient(135deg, #d9cbb6, var(--photo-warm) 60%, #6d5c4a); }
  .photo--cool { background: linear-gradient(135deg, #e4ecf2, var(--photo-cool) 55%, #4e6277); }
  .photo--office { background: linear-gradient(160deg, #f0f0ee, #bfc4c8 50%, #6c7378); }

  .group-name {
    position: absolute; left: 60px; top: 452px;
    display: flex; align-items: center; gap: 10px;
    font-weight: 600; font-size: 22px; color: var(--ink-grey);
  }
  .group-name .mark { width: 16px; height: 16px; background: var(--lime); }
  .contact {
    position: absolute; left: 60px; top: 498px;
    font-size: 14px; line-height: 19px; color: var(--ink-teal);
    font-style: normal;
  }
  .contact b { font-weight: 700; }

  .brand {
    position: absolute; left: 785px; top: 438px;
    display: flex; align-items: center; gap: 16px;
  }
  .brand-name {
    font-weight: 600; font-size: 50px; letter-spacing: -1px; color: var(--ink-grey);
  }
  .brand .mark { width: 40px; height: 40px; background: var(--lime); }
  .brand-tagline {
    position: absolute; left: 910px; top: 506px;
    font-size: 11px; font-weight: 600; color: var(--ink-grey);
  }
  .gutter {
    position: absolute; left: 549px; top: 0; width: 2px; height: 750px;
    background: linear-gradient(90deg, rgba(0,0,0,0.15), rgba(255,255,255,0.12));
  }
</style>
</head>
<body>
<main class="spread">
  <section class="page page--back"></section>
  <section class="page page--front"></section>

  <div class="band band--contact"></div>
  <div class="band band--title"></div>

  <div class="photo photo--office" style="left:440px;top:0;width:190px;height:200px" role="img" aria-label="Photo of two smiling professionals in business suits"></div>
  <div class="tile tile--graphite" style="left:630px;top:0;width:50px;height:40px"></div>
  <div class="tile tile--lime" style="left:395px;top:225px;width:52px;height:52px"></div>
  <div class="tile tile--graphite" style="left:518px;top:282px;width:52px;height:52px"></div>
  <div class="tile tile--lime" style="left:470px;top:340px;width:52px;height:52px"></div>
  <div class="tile tile--graphite" style="left:548px;top:390px;width:52px;height:52px"></div>

  <div class="photo photo--cool" style="left:698px;top:112px;width:102px;height:100px" role="img" aria-label="Photo of a woman working at an office desk with colleagues"></div>
  <div class="tile tile--lime" style="left:640px;top:240px;width:50px;height:50px"></div>
  <div class="tile tile--lime" style="left:694px;top:232px;width:50px;height:50px"></div>
  <div class="photo photo--warm" style="left:650px;top:292px;width:150px;height:92px" role="img" aria-label="Photo of colleagues meeting around a table"></div>
  <div class="photo photo--warm" style="left:800px;top:262px;width:80px;height:80px" role="img" aria-label="Photo of a smiling businessman"></div>
  <div class="tile tile--graphite" style="left:660px;top:390px;width:50px;height:50px"></div>
  <div class="tile tile--lime" style="left:716px;top:386px;width:50px;height:50px"></div>
  <div class="photo photo--office" style="left:585px;top:444px;width:175px;height:120px" role="img" aria-label="Photo of business people walking in a bright hallway"></div>

  <div class="tile tile--lime" style="left:478px;top:556px;width:52px;height:52px"></div>
  <div class="tile tile--lime" style="left:500px;top:626px;width:52px;height:52px"></div>

  <div class="group-name"><span class="mark"></span>Brightmere Group</div>
  <address class="contact">
    <b>Address Company</b><br>
    <b>City, Zip Code</b><br>
    <b>Phone:</b> 234.0148.2260<br>
    <b>Email:</b> info@brightmere.com<br>
    <b>Website:</b> www.brightmere.com
  </address>

  <div class="brand"><span class="brand-name">Tevaluma</span><span class="mark"></span></div>
  <div class="brand-tagline">by Brightmere Group</div>

  <div class="gutter"></div>
</main>
</body>
</html>
```